Kettle Ledger Business Card design

We need a stand out business card design for Accounting practice based in Australia specialising in pubs, clubs and hotels. We help venues maximise margins, create time and manage cashflow. One club we have been working with for the last 6 months has increased revenue by 3% and margin by 5% in this time frame. We have a back office outsourced system that costs less than having a full time employee and also allows the venues the added benefit of:<br/>-using the office space to become a revenue generating opportunity. <br/>-a complete system to enhance governance, accountability and efficiency within their operation<br/>-52 weeks cover so no hassle to cover annual/sick .. leave<br/><br/>We would like to see designs that use the colours of our logo (green & blue).
Target Market(s)
Australian Pubs, Clubs & Hotels abookkeeping, accounting and tax services
Industry/Entity Type
Accountant
Contact Information for Business Card
Miriam Oakley CPA
Principal
Accountant Tax Agent
Miriam@KettleLedger-example.com.au
0418693142
www.kettleledger-example.com.au
Accounting / Payroll / Tax / SMSF / Technology
Colors
Designer to choose colors to be used in the design.
Look and feel
Each slider illustrates characteristics of the customer's brand and the style your logo design should communicate.

```html
<!DOCTYPE html>
<html lang="en">
<head>
<meta charset="utf-8">
<title>Kettle Ledger Business Card</title>
<link rel="stylesheet" href="https://fonts.googleapis.com/css2?family=Poppins:wght@400;500;700;800&family=Roboto:wght@500&display=swap">
<style>
  :root {
    --brand-blue: #243f90;
    --brand-green: #166b3c;
    --leaf-green: #2e7a4a;
    --paper: #ffffff;
    --backdrop: #e9ebee;
  }
  * { box-sizing: border-box; margin: 0; padding: 0; }
  html, body { width: 1200px; height: 913px; overflow: hidden; }
  body {
    background: var(--backdrop);
    font-family: "Poppins", sans-serif;
    position: relative;
  }
  .card {
    position: absolute;
    left: 250px;
    width: 700px;
    height: 400px;
    overflow: hidden;
    box-shadow: 0 6px 18px rgba(0,0,0,0.18);
  }
  .card--front { top: 36px; background: var(--brand-blue); }
  .card--back { top: 477px; background: var(--paper); }

  /* Front */
  .front-brand {
    position: absolute;
    left: 0; right: 0; top: 120px;
    display: flex; align-items: center; justify-content: center; gap: 22px;
  }
  .brand-dot {
    width: 58px; height: 58px; border-radius: 50%;
    border: 6px solid var(--brand-green);
  }
  .front-brand .brand-name {
    color: var(--paper);
    font-weight: 800;
    font-size: 62px;
    line-height: 1;
    letter-spacing: -1px;
  }
  .front-url {
    position: absolute; left: 0; right: 0; top: 206px;
    text-align: center;
    color: var(--paper);
    font-family: "Roboto", sans-serif;
    font-weight: 500;
    font-size: 16px;
    letter-spacing: 1px;
    text-transform: uppercase;
    padding-left: 80px;
  }
  .service-band {
    position: absolute; left: 0; right: 0; bottom: 0;
    height: 58px;
    background: var(--brand-green);
    display: flex; align-items: center; justify-content: center;
    color: var(--paper);
    font-family: "Roboto", sans-serif;
    font-weight: 500;
    font-size: 17px;
    letter-spacing: 0.5px;
  }

  /* Back */
  .back-brand {
    position: absolute; left: 40px; top: 48px;
    display: flex; align-items: center; gap: 14px;
  }
  .back-brand .brand-dot { width: 40px; height: 40px; border-width: 4px; }
  .back-brand .brand-name {
    color: var(--brand-blue);
    font-weight: 800;
    font-size: 44px;
    line-height: 1;
    letter-spacing: -0.5px;
  }
  .person {
    position: absolute; left: 40px; top: 178px;
  }
  .person-name {
    color: var(--brand-blue);
    font-weight: 700;
    font-size: 30px;
    letter-spacing: 0.5px;
    line-height: 1.1;
  }
  .person-title {
    color: var(--brand-green);
    font-weight: 400;
    font-size: 17px;
    letter-spacing: 1.5px;
    margin-top: 2px;
  }
  .contacts {
    position: absolute; left: 40px; top: 262px;
    list-style: none;
  }
  .contacts li {
    display: flex; align-items: center; gap: 12px;
    color: var(--brand-blue);
    font-size: 17px;
    letter-spacing: 1px;
    line-height: 28px;
    text-transform: uppercase;
  }
  .contacts svg { width: 18px; height: 18px; fill: var(--brand-green); flex: none; }
  .back-bands { position: absolute; left: 0; bottom: 0; width: 700px; height: 60px; }
</style>
</head>
<body>

<section class="card card--front" aria-label="Card front">
  <div class="front-brand">
    <span class="brand-dot" aria-hidden="true"></span>
    <span class="brand-name">Kettle Ledger</span>
  </div>
  <p class="front-url">www.kettleledger-example.com.au</p>
  <div class="service-band">ACCOUNTING | PAYROLL | TAX | SMSF | TECHNOLOGY</div>
</section>

<section class="card card--back" aria-label="Card back">
  <div class="back-brand">
    <span class="brand-dot" aria-hidden="true"></span>
    <span class="brand-name">Kettle Ledger</span>
  </div>

  <div class="person">
    <h1 class="person-name">MIRIAM OAKLEY CPA</h1>
    <p class="person-title">PRINCIPAL ACCOUNTANT TAX AGENT</p>
  </div>

  <ul class="contacts">
    <li>
      <svg viewBox="0 0 24 24" aria-hidden="true"><path d="M6.6 10.8a15.1 15.1 0 0 0 6.6 6.6l2.2-2.2a1 1 0 0 1 1-.25 11.4 11.4 0 0 0 3.6.57 1 1 0 0 1 1 1V20a1 1 0 0 1-1 1A17 17 0 0 1 3 4a1 1 0 0 1 1-1h3.5a1 1 0 0 1 1 1c0 1.25.2 2.45.57 3.57a1 1 0 0 1-.25 1z"/></svg>
      0418693142
    </li>
    <li>
      <svg viewBox="0 0 24 24" aria-hidden="true"><path d="M2 5h20v14H2z M3.5 6.5 12 13l8.5-6.5" fill="none" stroke="currentColor"/><path d="M2 5h20v2l-10 7L2 7z"/><path d="M2 8.5l10 7 10-7V19H2z"/></svg>
      Miriam@KettleLedger-example.com.au
    </li>
    <li>
      <svg viewBox="0 0 24 24" aria-hidden="true"><path d="M12 2a10 10 0 1 0 0 20 10 10 0 0 0 0-20zm-1 17.9A8 8 0 0 1 4.2 10.6L9 15.4v1a2 2 0 0 0 2 2zm6.9-2.5A2 2 0 0 0 16 16h-1v-3a1 1 0 0 0-1-1H8v-2h2a1 1 0 0 0 1-1V7h2a2 2 0 0 0 2-2v-.4a8 8 0 0 1 2.9 12.8z"/></svg>
      www.kettleledger-example.com.au
    </li>
  </ul>

  <svg class="back-bands" viewBox="0 0 700 60" aria-hidden="true">
    <polygon points="0,48 430,48 430,60 0,60" fill="var(--brand-green)"/>
    <polygon points="430,22 700,0 700,60 420,60" fill="var(--brand-blue)"/>
    <polygon points="0,44 440,30 430,48 0,48" fill="var(--brand-green)" opacity="0"/>
  </svg>
</section>

</body>
</html>
```